Professional / Luxury Rack Card Design Needed (Do not use AI)

We are a private, boutique style optometry practice in College Station, Texas. We want the new design to communicate a premium, modern, luxury eye care experience while remaining professional and approachable.
When someone picks up this rack card, we want them to think:
"This practice looks modern, advanced, trustworthy, and premium. I would expect exceptional care and a high-end eyewear experience."

Target Market(s)

Families, professionals, adults seeking comprehensive medical eye care and vision correction. Patients seeking premium eyewear, advanced technology, and personalize care. Individuals and families seeking long term relationships with a trusted eye care provider. Patients who value exceptional service, expertise, and convenience.

Industry/Entity Type

Medical & Optometry-luxury optical

Font styles to use
Serif
Other font styles liked:
• Avenir if available. If not, Montserrat for headlines and Open Sans for Body text. For the slogan, use larger bold Montserrat.

Requirements
Must have
• Non-edited photo of doctors (merged together) with names. "Your Vision. Our Focus." Phone, website, Text/Call to Schedule appointment (Call to action to schedule). Accepting new patients. Eye Care center logo prominently displayed. Real photo of Eye Care Center building. Contact information (see attachement with all info)
Nice to have
• For frame brands, use the branded names. (see attachment)
Should not have
• Shouild not be busy/cluttered. Do not use scripted font from my website. Do NOT use AI generated images. Do not edit doctor faces other than merging them together. DO NOT use AI to edit faces....only to merge them side by side.

```html
<!DOCTYPE html>
<html lang="en">
<head>
<meta charset="utf-8">
<title>Clearview Eye Studio Rack Card</title>
<link href="https://fonts.googleapis.com/css2?family=Montserrat:ital,wght@0,300;0,400;0,500;0,600;0,700;0,800;1,400;1,800&family=Poppins:wght@400;500;600&display=swap" rel="stylesheet">
<style>
:root{
  --backdrop:#b5b7ba;
  --navy:#18232b;
  --gold:#dca321;
  --gold-band:#e7ab30;
  --sky:#a9dde9;
  --slate:#3b4f5e;
  --footer:#4a5968;
  --ink:#1d2329;
  --white:#ffffff;
  --offwhite:#f6f3f4;
}
*{box-sizing:border-box;margin:0;padding:0}
html,body{width:1073px;height:1200px;overflow:hidden;background:var(--backdrop)}
body{position:relative;font-family:"Montserrat",sans-serif}
.card{position:absolute;width:429px;height:965px;overflow:hidden;box-shadow:0 3px 8px rgba(0,0,0,.25)}
.card--front{left:94px;top:104px;background:var(--navy)}
.card--back{left:571px;top:108px;background:var(--white)}

/* front */
.building-photo{position:absolute;left:0;top:0;width:429px;height:520px;
  background:linear-gradient(180deg,#e9eef8 0%,#c9d3e6 22%,#c8ab7c 45%,#a98a62 70%,#5b5446 88%,var(--navy) 100%)}
.brand__dot{position:absolute;left:28px;top:30px;width:64px;height:64px;border-radius:50%;background:var(--sky);border:4px solid var(--slate)}
.brand__name{position:absolute;left:112px;top:34px;font-weight:400;font-size:25px;color:var(--slate);letter-spacing:.3px;line-height:28px;white-space:nowrap}
.brand__member{position:absolute;left:112px;top:70px;width:272px;font-size:8.5px;letter-spacing:2px;color:var(--slate);font-weight:500;border-top:1px solid #9aa5ae;padding-top:7px;white-space:nowrap}
.brand__member b{font-weight:500;font-size:15px;letter-spacing:1px;margin-left:6px}
.slogan{position:absolute;left:60px;top:462px;font-weight:800;font-size:80px;line-height:78px;letter-spacing:-2px;white-space:nowrap}
.slogan .line{display:block}
.slogan .light{color:var(--offwhite)}
.slogan .accent{color:var(--gold);font-style:italic}
.slogan .dot{color:var(--gold)}
.features{position:absolute;left:22px;top:800px;width:390px;display:flex}
.feature{flex:1;text-align:center;font-size:8.4px;font-weight:500;letter-spacing:.6px;color:var(--white);line-height:11.5px;border-right:1px solid #5d6a74;height:56px}
.feature:last-child{border-right:none;color:var(--gold)}
.feature svg{display:block;margin:0 auto 6px;height:26px}
.cta{position:absolute;left:82px;top:873px;width:263px;height:22px;background:var(--gold);color:var(--navy);font-weight:700;font-size:10.5px;letter-spacing:.8px;text-align:center;line-height:22px}
.accepting{position:absolute;left:0;width:100%;top:902px;text-align:center;font-style:italic;color:var(--white);font-size:10.5px;letter-spacing:.5px}

.contact{position:absolute;left:0;bottom:0;width:100%;height:45px;background:var(--footer);display:flex;align-items:center;padding:0 14px;color:var(--white);font-size:6.3px;letter-spacing:.4px;line-height:9px}
.contact__item{display:flex;align-items:center;gap:7px;padding:0 10px;border-right:1px solid #7c8893;height:22px}
.contact__item:first-child{padding-left:4px}
.contact__item:last-child{border-right:none}
.contact__item svg{width:14px;height:14px;flex:none}
.contact__item em{font-style:normal;color:var(--gold)}

/* back */
.tagline{position:absolute;top:27px;left:0;width:100%;text-align:center;font-weight:700;font-size:19px;letter-spacing:3px;line-height:25px;color:var(--slate)}
.tagline__rule{position:absolute;top:48px;width:51px;height:2px;background:var(--gold)}
.doctor{position:absolute;width:180px;text-align:center}
.doctor__photo{width:138px;height:138px;border-radius:50%;margin:0 auto;border:2px solid var(--gold);background:radial-gradient(circle at 50% 70%,#f1efee 0%,#cbbfae 45%,#8e806d 100%)}
.doctor__name{margin-top:10px;font-family:"Poppins",sans-serif;font-weight:500;font-size:15.5px;color:var(--ink)}
.service{position:absolute;left:0;width:100%;padding:24px 0 0 40px}
.service--medical{top:517px;height:230px;background:var(--sky)}
.service--vision{top:747px;height:175px;background:var(--gold-band)}
.service__head{display:flex;align-items:center;gap:12px;font-family:"Poppins",sans-serif;font-weight:500;font-size:17.5px;color:var(--slate)}
.service__cols{display:flex;margin-top:14px}
.service__col{width:170px;list-style:none}
.service__col li{display:flex;gap:9px;font-family:"Poppins",sans-serif;font-size:11px;color:var(--slate);line-height:13px;margin-bottom:15px}
.service__col li svg{flex:none;width:12px;height:12px;margin-top:1px}
.service--vision .service__col li{margin-bottom:13px}
.card--back .contact{height:44px}
</style>
</head>
<body>

<section class="card card--front">
  <div class="building-photo" role="img" aria-label="Photograph of the practice building with stone arches, stucco walls and tile roof at dusk"></div>
  <div class="brand__dot"></div>
  <div class="brand__name">Clearview Eye Studio</div>
  <div class="brand__member">A MEMBER OF<b>Optic Alliance</b></div>

  <h1 class="slogan">
    <span class="line light">Your</span>
    <span class="line light">Vision<span class="dot">.</span></span>
    <span class="line accent">Our</span>
    <span class="line accent">Focus.</span>
  </h1>

  <div class="features">
    <div class="feature">
      <svg viewBox="0 0 40 26" fill="none" stroke="#fff" stroke-width="1.4"><path d="M2 13C10 3 30 3 38 13C30 23 10 23 2 13Z"/><circle cx="20" cy="13" r="6"/><circle cx="20" cy="13" r="3"/></svg>
      COMPREHENSIVE<br>EYE CARE
    </div>
    <div class="feature">
      <svg viewBox="0 0 26 26" fill="none" stroke="#fff" stroke-width="1.4"><circle cx="13" cy="13" r="11"/><circle cx="13" cy="13" r="6"/><circle cx="13" cy="13" r="2.6" fill="#dca321" stroke="none"/><path d="M13 0v4M13 22v4M0 13h4M22 13h4"/></svg>
      ADVANCED<br>TECHNOLOGY
    </div>
    <div class="feature">
      <svg viewBox="0 0 26 26" fill="none" stroke="#dca321" stroke-width="1.4"><circle cx="13" cy="8" r="6"/><path d="M2 25c0-7 5-10 11-10s11 3 11 10z"/></svg>
      PERSONALIZED<br>CARE
    </div>
    <div class="feature">
      <svg viewBox="0 0 44 26" fill="none" stroke="#dca321" stroke-width="1.6"><circle cx="11" cy="14" r="8"/><circle cx="33" cy="14" r="8"/><path d="M19 13c2-2 4-2 6 0M3 11 1 8M41 11l2-3"/></svg>
      OVER 1,000<br>DESIGNER FRAMES<br>&amp; SUNGLASSES
    </div>
  </div>

  <div class="cta">SCHEDULE YOUR APPOINTMENT TODAY</div>
  <p class="accepting">Accepting New Patients</p>

  <footer class="contact">
    <div class="contact__item">
      <svg viewBox="0 0 14 14" fill="none" stroke="#dca321" stroke-width="1"><path d="M7 13s4.5-4.5 4.5-7.5a4.5 4.5 0 0 0-9 0C2.5 8.5 7 13 7 13z"/><circle cx="7" cy="5.5" r="1.6"/></svg>
      <span>418 MEADOW RIDGE DR<br>BROOKFIELD, TX 77010</span>
    </div>
    <div class="contact__item">
      <svg viewBox="0 0 14 14" fill="none" stroke="#dca321" stroke-width="1"><path d="M3 1.5 5 4 4 5.5c.8 1.8 2.5 3.5 4.5 4.5L10 9l2.5 2-1.3 1.8C6.5 12.5 1.5 7.5 1.2 2.8z"/></svg>
      <span>CALL OR TEXT<br>555.014.2200</span>
    </div>
    <div class="contact__item">
      <svg viewBox="0 0 14 14" fill="none" stroke="#dca321" stroke-width="1"><circle cx="7" cy="7" r="6"/><ellipse cx="7" cy="7" rx="2.6" ry="6"/><path d="M1 7h12M2 4h10M2 10h10"/></svg>
      <span>MAKE YOUR APPOINTMENT ONLINE<br>WWW.<em>CLEARVIEWEYESTUDIO.COM</em></span>
    </div>
  </footer>
</section>

<section class="card card--back">
  <span class="tagline__rule" style="left:32px"></span>
  <h2 class="tagline">EXPERT EYE CARE.<br>PERSONAL TOUCH.</h2>
  <span class="tagline__rule" style="left:351px"></span>

  <div class="doctor" style="left:26px;top:113px">
    <div class="doctor__photo" role="img" aria-label="Portrait of Dr. Harlow in a white coat in front of a stone wall"></div>
    <p class="doctor__name">Dr.Harlow, O.D</p>
  </div>
  <div class="doctor" style="left:206px;top:113px">
    <div class="doctor__photo" role="img" aria-label="Portrait of Dr. Pennick in a white coat in front of a stone wall"></div>
    <p class="doctor__name">Dr.Pennick, O.D</p>
  </div>
  <div class="doctor" style="left:24px;top:314px">
    <div class="doctor__photo" role="img" aria-label="Portrait of Dr. Wexley in a white coat in front of a stone wall"></div>
    <p class="doctor__name">Dr.Wexley, O.D</p>
  </div>
  <div class="doctor" style="left:206px;top:314px">
    <div class="doctor__photo" role="img" aria-label="Portrait of Dr. Marone in a white coat in front of a stone wall"></div>
    <p class="doctor__name">Dr.Marone, O.D</p>
  </div>

  <div class="service service--medical">
    <div class="service__head">
      <svg width="36" height="22" viewBox="0 0 36 22" fill="none" stroke="#3b4f5e" stroke-width="1.4"><path d="M1 11C8 2 28 2 35 11C28 20 8 20 1 11Z"/><circle cx="18" cy="11" r="6"/><circle cx="18" cy="11" r="3"/></svg>
      MEDICAL EYE CARE
    </div>
    <div class="service__cols">
      <ul class="service__col">
        <li><svg viewBox="0 0 12 12"><path d="M1 6.5 4.5 10 11 2" fill="none" stroke="#dca321" stroke-width="2"/></svg>Cataract</li>
        <li><svg viewBox="0 0 12 12"><path d="M1 6.5 4.5 10 11 2" fill="none" stroke="#dca321" stroke-width="2"/></svg>Glaucoma</li>
        <li><svg viewBox="0 0 12 12"><path d="M1 6.5 4.5 10 11 2" fill="none" stroke="#dca321" stroke-width="2"/></svg>Macular Degeneration</li>
        <li><svg viewBox="0 0 12 12"><path d="M1 6.5 4.5 10 11 2" fill="none" stroke="#dca321" stroke-width="2"/></svg>Dry Eye &amp; Allergy</li>
        <li><svg viewBox="0 0 12 12"><path d="M1 6.5 4.5 10 11 2" fill="none" stroke="#dca321" stroke-width="2"/></svg>Eye Injuries &amp; Infections</li>
      </ul>
      <ul class="service__col">
        <li><svg viewBox="0 0 12 12"><path d="M1 6.5 4.5 10 11 2" fill="none" stroke="#dca321" stroke-width="2"/></svg>Ocular Disease<br>Management</li>
        <li><svg viewBox="0 0 12 12"><path d="M1 6.5 4.5 10 11 2" fill="none" stroke="#dca321" stroke-width="2"/></svg>Surgery Co-Management</li>
        <li><svg viewBox="0 0 12 12"><path d="M1 6.5 4.5 10 11 2" fill="none" stroke="#dca321" stroke-width="2"/></svg>Migraine &amp; Headache</li>
        <li><svg viewBox="0 0 12 12"><path d="M1 6.5 4.5 10 11 2" fill="none" stroke="#dca321" stroke-width="2"/></svg>Eye Muscle Alignment</li>
      </ul>
    </div>
  </div>

  <div class="service service--vision">
    <div class="service__head">
      <svg width="42" height="20" viewBox="0 0 42 20" fill="none" stroke="#1d2329" stroke-width="1.8"><circle cx="11" cy="11" r="8"/><circle cx="31" cy="11" r="8"/><path d="M19 10c1.5-1.5 2.5-1.5 4 0M3 8 1 5M39 8l2-3"/></svg>
      VISION SERVICES
    </div>
    <div class="service__cols">
      <ul class="service__col">
        <li><svg viewBox="0 0 12 12"><path d="M1 6.5 4.5 10 11 2" fill="none" stroke="#3b4f5e" stroke-width="2"/></svg>Comprehensive<br>Eye Exams</li>
        <li><svg viewBox="0 0 12 12"><path d="M1 6.5 4.5 10 11 2" fill="none" stroke="#3b4f5e" stroke-width="2"/></svg>Pediatric Exams</li>
        <li><svg viewBox="0 0 12 12"><path d="M1 6.5 4.5 10 11 2" fill="none" stroke="#3b4f5e" stroke-width="2"/></svg>Specialty Contact<br>Lens Service</li>
      </ul>
      <ul class="service__col">
        <li><svg viewBox="0 0 12 12"><path d="M1 6.5 4.5 10 11 2" fill="none" stroke="#3b4f5e" stroke-width="2"/></svg>Advanced Diagnostic<br>Testing</li>
        <li><svg viewBox="0 0 12 12"><path d="M1 6.5 4.5 10 11 2" fill="none" stroke="#3b4f5e" stroke-width="2"/></svg>Surgery Co-Management</li>
        <li><svg viewBox="0 0 12 12"><path d="M1 6.5 4.5 10 11 2" fill="none" stroke="#3b4f5e" stroke-width="2"/></svg>Eye Muscle Alignment</li>
      </ul>
    </div>
  </div>

  <footer class="contact">
    <div class="contact__item">
      <svg viewBox="0 0 14 14" fill="none" stroke="#dca321" stroke-width="1"><path d="M7 13s4.5-4.5 4.5-7.5a4.5 4.5 0 0 0-9 0C2.5 8.5 7 13 7 13z"/><circle cx="7" cy="5.5" r="1.6"/></svg>
      <span>418 MEADOW RIDGE DR<br>BROOKFIELD, TX 77010</span>
    </div>
    <div class="contact__item">
      <svg viewBox="0 0 14 14" fill="none" stroke="#dca321" stroke-width="1"><path d="M3 1.5 5 4 4 5.5c.8 1.8 2.5 3.5 4.5 4.5L10 9l2.5 2-1.3 1.8C6.5 12.5 1.5 7.5 1.2 2.8z"/></svg>
      <span>CALL OR TEXT<br>555.014.2200</span>
    </div>
    <div class="contact__item">
      <svg viewBox="0 0 14 14" fill="none" stroke="#dca321" stroke-width="1"><circle cx="7" cy="7" r="6"/><ellipse cx="7" cy="7" rx="2.6" ry="6"/><path d="M1 7h12M2 4h10M2 10h10"/></svg>
      <span>MAKE YOUR APPOINTMENT ONLINE<br>WWW.<em>CLEARVIEWEYESTUDIO.COM</em></span>
    </div>
  </footer>
</section>

</body>
</html>
```